Flyer Required for Economics Tuition business in Singapore

Require a 4-page, A4 bi-fold full colour flyer. To use attractive & vibrant colours. Can make use of colour schemes and design layouts from upcoming website revamp: http://lessonbrightpath.com/Website/
Target audience for the flyer will be 17 - 18 years old A Level students in Singapore studying in Junior Colleges.
I have attached the detailed design brief with the content required for the flyer as a file titled "Design Brief.docx" & also the logo for our business to be used in the flyer & optional photos that can be used in the flyer
Reason: Require more designs. Current designs provided are too "template" like

```html
<!DOCTYPE html>
<html lang="en">
<head>
<meta charset="utf-8">
<title>Lesson Bright Path – Economics Tuition Flyer</title>
<link href="https://fonts.googleapis.com/css2?family=Open+Sans:ital,wght@0,400;0,600;0,700;0,800;1,400&display=swap" rel="stylesheet">
<style>
  :root{
    --blue:#29a8e0;
    --orange:#f7941d;
    --orange-deep:#ee8312;
    --green:#1a9a48;
    --red:#c8102e;
    --ink:#3b3b3b;
    --grey:#5c5c5c;
    --paper:#ffffff;
    --stage:#eceeef;
  }
  *{box-sizing:border-box;margin:0;padding:0}
  html,body{width:982px;height:1200px;overflow:hidden}
  body{background:var(--stage);font-family:"Open Sans",sans-serif;color:var(--ink);position:relative}

  .spread{position:absolute;left:71px;width:840px;height:580px;display:flex;box-shadow:0 4px 14px rgba(0,0,0,.18)}
  .spread--inside{top:13px}
  .spread--outside{top:607px}
  .panel{position:relative;width:420px;height:580px;overflow:hidden;background:var(--paper)}

  /* ---------- Profile panel ---------- */
  .profile-top{background:var(--blue);padding:16px 20px 0}
  .profile h2{font-size:15px;font-weight:600;line-height:1.2;margin-bottom:4px}
  .profile-top h2{color:#fff}
  .profile-top p{color:#fff;font-size:6.8px;line-height:1.5;margin-bottom:10px}
  .profile-photo{height:112px;margin:4px -20px 0;background:linear-gradient(120deg,#e6e2dc 0%,#b9b2ac 40%,#5d5a63 75%,#2f2d33 100%)}
  .profile-body{padding:14px 20px 0}
  .profile-body h2{color:var(--blue)}
  .profile-body p{color:var(--grey);font-size:6.8px;line-height:1.5;margin-bottom:9px}
  .classroom-photo{position:absolute;left:0;right:0;bottom:0;height:150px;background:linear-gradient(100deg,#f0d9c4 0%,#c88f6c 35%,#6b4a3d 70%,#2c2522 100%)}

  /* ---------- Testimonials panel ---------- */
  .group-photos{display:flex;gap:4px;height:116px;padding:6px 6px 0}
  .group-photo{flex:1;background:linear-gradient(180deg,#e9e7e4 0%,#c9c2bb 45%,#3a3840 100%)}
  .group-photo--sofa{background:linear-gradient(180deg,#f1f0ee 0%,#d7d1ca 50%,#4d4b52 100%)}
  .band{color:#fff;font-weight:700;text-transform:uppercase;letter-spacing:.2px}
  .band--green{background:var(--green)}
  .band--red{background:var(--red)}
  .band--blue{background:var(--blue)}
  .testimonials .band{margin-top:6px;height:22px;line-height:22px;text-align:center;font-size:10px}
  .quotes{padding:10px 20px 0;list-style:none}
  .quote{border-bottom:1px solid #e2e2e2;padding-bottom:5px;margin-bottom:7px}
  .quote:last-child{border-bottom:0}
  .quote p{font-style:italic;font-size:7px;line-height:1.45;color:var(--grey)}
  .quote cite{display:block;text-align:right;font-style:normal;font-size:6px;color:var(--grey);margin-top:3px}
  .quote cite b{color:var(--orange);font-weight:700}

  /* ---------- Schedule panel ---------- */
  .schedule{background:linear-gradient(170deg,var(--orange) 0%,var(--orange-deep) 100%);color:#fff;padding:18px 22px 0}
  .schedule h2{font-size:14px;font-weight:800;text-transform:uppercase;margin-bottom:6px}
  .timetables{display:flex;gap:10px}
  .timetable{border-collapse:collapse;flex:1;background:#fff;color:var(--ink);font-size:7px}
  .timetable td{border:1px solid #f6b86b;height:15px;padding:0 5px;white-space:nowrap}
  .schedule-note{font-size:8px;font-weight:700;line-height:1.35;margin:8px 0 14px}
  .schedule-note span{font-weight:400;font-size:7px;display:block}
  .locations{list-style:none;margin:4px 0 12px}
  .locations li{display:flex;gap:7px;font-size:7.2px;line-height:1.4;margin-bottom:6px}
  .locations .num{flex:none;width:13px;height:13px;border:1px solid #fff;border-radius:50%;font-size:7px;text-align:center;line-height:11px}
  .fees p{font-size:8px;line-height:1.55}
  .schedule .band{position:absolute;left:0;right:0;bottom:0;height:42px;line-height:42px;text-align:center;font-size:17px;text-transform:none}

  /* ---------- Cover panel ---------- */
  .cover{padding:22px 22px 0}
  .cover-photo{position:absolute;inset:0;background:linear-gradient(160deg,#ffffff 0%,#ffffff 30%,#eef0f2 60%,#dcdfe3 100%)}
  .cover > *:not(.cover-photo){position:relative}
  .brand{display:flex;align-items:center;justify-content:center;gap:7px;margin-bottom:10px}
  .brand-mark{width:16px;height:16px;background:var(--orange)}
  .brand-name{font-size:19px;font-weight:700;color:var(--orange)}
  .headline{font-size:15px;font-weight:800;line-height:1.2;color:var(--ink);margin-bottom:9px}
  .headline em{font-style:normal;color:var(--orange)}
  .cover .band{height:18px;line-height:18px;padding-left:8px;font-size:8.5px;margin:8px 0 6px}
  .cover p{font-size:7px;line-height:1.5;color:var(--ink);margin-bottom:5px}
</style>
</head>
<body>

<!-- Inside spread -->
<section class="spread spread--inside">
  <article class="panel profile">
    <div class="profile-top">
      <h2>Background</h2>
      <p>Mr Tan is the founder of Lesson Bright Path and has taught A Level Economics for over ten years, guiding hundreds of students from junior colleges across Singapore to strong results.</p>
      <h2>Academic Qualifications</h2>
      <p>Mr Tan holds a first class honours degree in Economics and a postgraduate diploma in education. He was awarded a teaching scholarship and served as an Economics teacher in a junior college.</p>
      <div class="profile-photo" role="img" aria-label="Photo of Mr Tan with a group of students"></div>
    </div>
    <div class="profile-body">
      <h2>Teaching Experience</h2>
      <p>Mr Tan taught Economics in a junior college from 2007 to 2012 and later marked national examination scripts. His students have consistently scored distinctions, with many improving by two or more grades within a single year of lessons.</p>
      <h2>Style of Teaching</h2>
      <p>Mr Tan's lessons break difficult concepts into clear frameworks, supported by current local examples that examiners reward. Students practise essay planning and case study answers every week with detailed feedback.</p>
      <p>Classes are kept small so that every student is heard, and notes are updated each year.</p>
    </div>
    <div class="classroom-photo" role="img" aria-label="Photo of students during a tuition class"></div>
  </article>

  <article class="panel testimonials">
    <div class="group-photos">
      <div class="group-photo" role="img" aria-label="Group photo of a tuition class"></div>
      <div class="group-photo group-photo--sofa" role="img" aria-label="Group photo of students seated on a sofa"></div>
    </div>
    <h2 class="band band--green">Testimonials from Students</h2>
    <ul class="quotes">
      <li class="quote"><p>"Mr Tan really has all his students' interests at heart. He buys dinner for us, provides us with mini snacks, incentivises us with great rewards, there was also once where he bought me some flu medicine because I was suffering from a bad cold. Thank you Mr Tan!"</p><cite><b>-Lim Wen Hui</b> Northbridge Junior College</cite></li>
      <li class="quote"><p>Mr Tan is a very friendly teacher who ensures that his students receive the best. He spends a lot of effort in preparing for lessons such as finding articles that are relevant to the subject and coming up with different ways to help us learn better.</p><cite><b>-Koh Jun</b> Harbourview Junior College</cite></li>
      <li class="quote"><p>Mr Tan's lessons are very engaging and fun. It's a very different and beneficial tuition style that will definitely benefit students. Content was covered very effectively and thoroughly for each lesson and made easy to understand by Mr Tan's effective teaching methods and anecdotal examples. There is a very comfortable environment here as well, especially as there are free refreshments. It has been very enjoyable being in this tuition and Mr Tan is a wonderful tutor.</p><cite><b>-Stella Goh</b> Riverside Heights School</cite></li>
      <li class="quote"><p>Even though I have only been working with Mr Tan for a few months, I have learnt many different skills and specific Singaporean examples that are essential for a good economics grade, but not covered in school classes. Mr Tan also has amazing stories to tell, and I personally am inspired by his story.</p><cite><b>-Karen Lau</b> Lakeside Institution</cite></li>
      <li class="quote"><p>Mr Tan and the tuition centre have greatly improved my quality of work in economics, and his knowledge and insights provided during lessons were very valuable to me as an econs student. I was able to perform well in almost all my examinations after attending lessons and this gave me confidence moving on to A levels. I would recommend the tuition centre to those in need of help in econs. You can acquire relevant skills in essays and CSQ which I believe will help me pull through A levels with ease.</p><cite><b>-Max Teo</b> Parkway Junior College</cite></li>
    </ul>
  </article>
</section>

<!-- Outside spread -->
<section class="spread spread--outside">
  <article class="panel schedule">
    <h2>Class Schedule*</h2>
    <div class="timetables">
      <table class="timetable">
        <tr><td>JC2 Monday 5pm</td><td>Jurong West</td></tr>
        <tr><td>JC2 Monday 7pm</td><td>Jurong West</td></tr>
        <tr><td>JC2 Tuesday 5:30pm</td><td>Clementi</td></tr>
        <tr><td>JC1 Tuesday 7:30pm</td><td>Clementi</td></tr>
        <tr><td>JC2 Wednesday 6pm</td><td>Bedok</td></tr>
        <tr><td>JC2 Wednesday 8pm</td><td>Bedok</td></tr>
        <tr><td>JC2 Thursday 5:30pm</td><td>Choa Chu Kang</td></tr>
        <tr><td>JC1 Thursday 7:30pm</td><td>Choa Chu Kang</td></tr>
      </table>
      <table class="timetable">
        <tr><td>JC2 Saturday 10am</td><td>Choa Chu Kang</td></tr>
        <tr><td>JC2 Saturday 12pm</td><td>Choa Chu Kang</td></tr>
        <tr><td>JC1 Saturday 2pm</td><td>Choa Chu Kang</td></tr>
        <tr><td>JC2 Saturday 4pm</td><td>Choa Chu Kang</td></tr>
        <tr><td>JC2 Sunday 10am</td><td>Choa Chu Kang</td></tr>
        <tr><td>JC2 Sunday 12pm</td><td>Choa Chu Kang</td></tr>
        <tr><td>JC1 Sunday 2pm</td><td>Choa Chu Kang</td></tr>
        <tr><td>JC2 Sunday 4pm</td><td>Choa Chu Kang</td></tr>
      </table>
    </div>
    <p class="schedule-note">*MOST Classes are already full. Call/SMS/Message us at 80001234<span>to confirm available timings.</span></p>

    <h2>Our Locations</h2>
    <ol class="locations">
      <li><span class="num">1</span><span>Choa Chu Kang: Blk 118 Choa Chu Kang Ave 3 #01-210<br>2 minutes walk from CCK MRT</span></li>
      <li><span class="num">2</span><span>Clementi: Blk 330 Clementi Ave 2 #01-145 (2nd storey)<br>5 min bus ride from Clementi MRT</span></li>
      <li><span class="num">3</span><span>Bedok: Blk 540 Bedok North Street 2 #01-77<br>7 minutes walk from Bedok MRT</span></li>
      <li><span class="num">4</span><span>Jurong West: Jurong West Ave 4, opposite the petrol station<br>5 minutes bus ride from Jurong East MRT</span></li>
    </ol>

    <div class="fees">
      <h2>Fees &amp; Promotions</h2>
      <p>$295 per month – JC2s<br>$280 per month – JC1s (early bird promotion)<br>Sign up with a friend(s) to enjoy $20 off monthly fees.</p>
    </div>
    <p class="band band--red">Text/Call/Message us at 80001234</p>
  </article>

  <article class="panel cover">
    <div class="cover-photo" role="img" aria-label="Faint background photo of students in class"></div>
    <div class="brand"><span class="brand-mark"></span><span class="brand-name">Lesson Bright Path</span></div>
    <h1 class="headline"><em>Failing Economics?</em> It's time to get the RIGHT help for your A Level Economics!</h1>

    <h2 class="band band--red">Singapore's Leading Economics Tuition Programme</h2>
    <p>The Economics programme at Lesson Bright Path is a structured two-year course for A Level students, built around the syllabus with thematic notes, timed practice and revision seminars before the examinations.</p>
    <p>All classes are taught by Mr Tan, who has taught over 1,000 students since 2007. More than 90% of his students improve by at least two grades.</p>

    <h2 class="band band--blue">Why Join Us!</h2>
    <p>Since 2007, Mr Tan has been teaching Economics full time and understands exactly what examiners look for in essays and case studies across Singapore.</p>
    <p>For the latest A Level results, 18 students scored A and 12 scored B.</p>

    <h2 class="band band--green">Testimonials of Students</h2>
    <p>Before I joined this tuition, economics was something I always dreaded. Mr Tan explained every topic patiently and gave me the confidence to write clear essays.</p>
    <p>As a student who had only gone for tuition since JC1, I found the lessons well planned and the notes easy to revise from. Thanks Mr Tan!</p>
  </article>
</section>

</body>
</html>
```